Window Decal for Speech, Feeding, Occupational, Physical, and Behavior Therapy office for children

I need a high resolution, vertical design, preferably via Adobe Illustrator (real size design) that can be applied to office store front windows, in the form of window decals. The business is called Bright Steps Therapy and we provide Speech, Feeding, Occupational, Physical and Behavior Therapy for children; therefore, the design must be relay a kid-friendly image, while highlighting conditions we treat/service. We are looking to apply signage to (4) glass windows and (1) glass entry door. I have uploaded (3) attachments - a draft design (with window measurements), our company logo and an image of the store front.

Target Market(s)

Parents

Industry/Entity Type

Healthcare

Colors

Designer to choose colors to be used in the design.

Requirements
Must have
• Imagery must be high resolution
• The logo is trademarked, so it must stay the same.
• The (3) window design of the faces blowing bubbles, with the depicted wording is necessary; however, the imagery and layout can both be improved upon, yet I still need a resemblance to what is provided. Additionally, I've added (2) new facial images from the interior walls of our clinic. My preference is to have the faces for the exterior windows mirror these images as closely as possible in terms of skin tone (darkness), definition and realism.
• Also, please provide bleed room along the edges in your design.

```html
<!DOCTYPE html>
<html lang="en">
<head>
<meta charset="utf-8">
<title>Is Your Child On Track? – Window Decal</title>
<link rel="stylesheet" href="https://fonts.googleapis.com/css2?family=Open+Sans:wght@400;700;800&display=swap">
<style>
  :root {
    --teal: #0b9e88;
    --teal-soft: #5cb5a2;
    --aqua: #46bcc3;
    --aqua-ring: #c9e8e2;
    --purple: #7d3f98;
    --yellow: #fff200;
    --lime: #dde03c;
    --leaf: #85b96e;
    --white: #ffffff;
    --mist: #d7ede8;
    --picky: #2aa89e;
  }
  html, body {
    margin: 0;
    padding: 0;
    width: 1200px;
    height: 855px;
    overflow: hidden;
    background: var(--white);
  }
  .decal {
    display: block;
    width: 1200px;
    height: 855px;
    font-family: "Open Sans", Verdana, sans-serif;
  }
  .panel { fill: var(--teal); }
  .dot-soft { fill: var(--teal-soft); opacity: .85; }
  .dot-mist { fill: var(--mist); opacity: .75; }
  .ring-faint { fill: none; stroke: var(--aqua-ring); stroke-width: 3; opacity: .6; }
  .label-bold { font-weight: 700; }
  .label-light { font-weight: 400; }
  .on-white { fill: var(--purple); }
  .on-dark { fill: var(--white); }
  .tagline { fill: var(--white); font-weight: 700; font-size: 22px; letter-spacing: .5px; }
</style>
</head>
<body>
<svg class="decal" viewBox="0 0 1200 855" xmlns="http://www.w3.org/2000/svg">
  <defs>
    <clipPath id="panel-left"><rect x="10" y="10" width="390" height="835"/></clipPath>
    <clipPath id="panel-middle"><rect x="406" y="10" width="388" height="835"/></clipPath>
    <clipPath id="panel-right"><rect x="800" y="10" width="390" height="835"/></clipPath>
  </defs>

  <!-- Window panels -->
  <rect class="panel" x="10" y="10" width="390" height="835"/>
  <rect class="panel" x="406" y="10" width="388" height="835"/>
  <rect class="panel" x="800" y="10" width="390" height="835"/>

  <!-- Left panel -->
  <g class="panel-left" clip-path="url(#panel-left)">
    <circle class="dot-soft" cx="345" cy="108" r="42"/>
    <g class="bubble-balance">
      <path d="M215 222 L272 262 L250 212 Z" fill="var(--white)"/>
      <circle cx="150" cy="105" r="152" fill="var(--white)"/>
      <circle cx="140" cy="95" r="142" fill="var(--teal)"/>
      <text x="142" y="84" text-anchor="middle" class="on-dark label-bold" font-size="31">Balance</text>
      <text x="142" y="124" text-anchor="middle" class="on-dark label-light" font-size="30">and</text>
      <text x="142" y="164" text-anchor="middle" class="on-dark label-bold" font-size="31">Coordination</text>
    </g>
    <circle cx="125" cy="410" r="78" fill="var(--yellow)"/>
    <circle cx="131" cy="412" r="66" fill="var(--teal)"/>
    <circle class="dot-mist" cx="347" cy="792" r="30"/>
  </g>

  <!-- Speech Delay -->
  <g class="bubble-speech">
    <path d="M392 508 C380 570 340 610 280 630 L240 585 Z" fill="var(--purple)"/>
    <circle cx="190" cy="675" r="128" fill="var(--purple)"/>
    <text x="185" y="680" text-anchor="middle" class="on-dark label-bold" font-size="44">Speech</text>
    <text x="185" y="733" text-anchor="middle" class="on-dark label-light" font-size="42">Delay</text>
  </g>
  <circle cx="222" cy="535" r="58" fill="var(--white)" opacity=".3" clip-path="url(#panel-left)"/>

  <!-- Middle panel -->
  <g class="panel-middle" clip-path="url(#panel-middle)">
    <circle cx="540" cy="95" r="60" fill="var(--aqua)" stroke="var(--aqua-ring)" stroke-width="5"/>
    <circle cx="728" cy="45" r="30" fill="var(--lime)"/>
    <circle class="ring-faint" cx="505" cy="662" r="74"/>
    <circle class="ring-faint" cx="518" cy="667" r="66"/>
    <circle class="dot-soft" cx="632" cy="695" r="27"/>
    <text x="603" y="780" text-anchor="middle" class="tagline">EARLY INTERVENTION</text>
    <text x="603" y="810" text-anchor="middle" class="tagline">MATTERS</text>
  </g>

  <!-- Toe Walking -->
  <g class="bubble-toe">
    <path d="M615 312 C650 322 680 315 700 300 L690 270 Z" fill="var(--white)"/>
    <circle cx="765" cy="208" r="112" fill="var(--white)"/>
    <text x="778" y="202" text-anchor="middle" class="on-white label-bold" font-size="29">Toe</text>
    <text x="778" y="245" text-anchor="middle" class="on-white label-bold" font-size="29">Walking</text>
  </g>

  <!-- Stuttering -->
  <g class="bubble-stutter">
    <path d="M505 528 C535 570 575 585 610 580 L620 520 Z" fill="var(--white)"/>
    <circle cx="725" cy="550" r="130" fill="var(--white)"/>
    <text x="725" y="568" text-anchor="middle" class="on-white label-bold" font-size="34">Stuttering</text>
  </g>

  <!-- Central headline -->
  <g class="headline">
    <circle cx="431" cy="346" r="196" fill="var(--white)"/>
    <circle cx="431" cy="346" r="186" fill="none" stroke="var(--purple)" stroke-width="5"/>
    <text x="431" y="302" text-anchor="middle" class="on-white" font-weight="800" font-size="38">IS YOUR</text>
    <text x="431" y="390" text-anchor="middle" class="on-white" font-weight="800" font-size="82">CHILD</text>
    <text x="431" y="455" text-anchor="middle" class="on-white" font-weight="800" font-size="38">ON TRACK?</text>
  </g>

  <!-- Right panel -->
  <g class="panel-right" clip-path="url(#panel-right)">
    <circle class="dot-soft" cx="1140" cy="262" r="60"/>
    <g class="bubble-autism">
      <path d="M848 188 C890 200 930 195 960 180 L955 150 Z" fill="var(--purple)"/>
      <circle cx="1062" cy="95" r="145" fill="var(--purple)"/>
      <text x="1068" y="130" text-anchor="middle" class="on-dark label-bold" font-size="58">Autism</text>
    </g>
    <g class="bubble-social">
      <path d="M822 524 C860 540 895 530 915 505 L890 480 Z" fill="var(--yellow)"/>
      <circle cx="985" cy="408" r="130" fill="var(--yellow)"/>
      <circle cx="978" cy="410" r="119" fill="var(--teal)"/>
      <text x="980" y="405" text-anchor="middle" class="on-dark label-bold" font-size="52">Social</text>
      <text x="980" y="470" text-anchor="middle" class="on-dark label-light" font-size="50">Skills</text>
    </g>
    <g class="bubble-picky">
      <circle cx="1088" cy="690" r="132" fill="var(--picky)" stroke="var(--aqua-ring)" stroke-width="5" stroke-opacity=".6"/>
      <text x="1088" y="685" text-anchor="middle" class="label-bold" fill="var(--mist)" font-size="38">Picky</text>
      <text x="1088" y="732" text-anchor="middle" class="label-light" fill="var(--mist)" font-size="38">Eater</text>
    </g>
    <circle cx="888" cy="718" r="52" fill="var(--leaf)" opacity=".9"/>
    <circle class="dot-soft" cx="932" cy="800" r="26"/>
  </g>
</svg>
</body>
</html>
```